Technology solutions catalog

Were looking for a catalogue to supplement our website and corporate branding.

Our website will give you a good understanding of our products and services as well as our theme.

Our base colour and logo is red, white and grey.

www.voltrane.com.au

The aim of the catalogue is to showcase our business IT services & solutions. This will be a mix of education about the new solutions available to small and medium business today and how these solutions can increase productivity.

We would also like tip sections

This isn't all about selling but also about educating SMB's of the new and exciting IT solutions available today and having them book a free consult with us to discuss further about how we can help the business.

Solutions and area's that the catalogue will need to cover include

Front Cover -
-About us section, with our business contact information (1st page)
- Introduction. (2nd page)
-Communication Solutions - this includes Email, IP phones and business IT networks (2 pages)
- Data & Storage solutions (2 pages)
- Hardware (1 pages)
- Business IT health check list (1 page)
- Services and support offering (2 pages)
- Software & Popular cloud solutions (2 pages)
- Website / E-commerce solutions (2 pages)
Back cover

Based on two pages per solution the whole catalogue will be around 14 pages.

We don't need any text content done. We would like Headings on pages including page numbers. Footer please.

We're looking for a template that we can have our designer finish off by adding in some further product and service image and text.

Thank you for your consideration

Target Market(s)

IT for small and medium businesses

Industry/Entity Type

Supplement

Requirements
Must have
• Size A4
• Design supplied in Adobe indesign so we can edit and add our text and content
• Clean design

```html
<!DOCTYPE html>
<html lang="en">
<head>
<meta charset="utf-8">
<title>Voltrane – Technology Solutions Catalogue</title>
<link href="https://fonts.googleapis.com/css2?family=Open+Sans:ital,wght@0,300;0,400;0,600;0,700;0,800;1,300&display=swap" rel="stylesheet">
<style>
  :root {
    --red: #c41f2a;
    --red-light: #d4505b;
    --red-dark: #9e1820;
    --page: #ececed;
    --page-light: #f6f6f6;
    --ink: #666a6e;
    --ink-dark: #3f4347;
    --slate: #5f666c;
    --white: #ffffff;
    --canvas: #ffffff;
  }
  * { box-sizing: border-box; margin: 0; padding: 0; }
  html, body { width: 1200px; height: 2400px; overflow: hidden; background: var(--canvas); }
  body { font-family: "Open Sans", Arial, sans-serif; color: var(--ink); }
  .canvas { position: relative; width: 1200px; height: 2400px; overflow: hidden; }

  .brand-title {
    position: absolute; top: 62px; left: 0; width: 1200px; text-align: center;
    font-weight: 800; font-size: 62px; color: var(--red); letter-spacing: 0.5px;
  }

  .page { position: absolute; overflow: hidden; box-shadow: 0 6px 18px rgba(0,0,0,0.18); }
  .spread { position: absolute; width: 760px; height: 270px; box-shadow: 0 6px 18px rgba(0,0,0,0.18); }
  .spread .page { box-shadow: none; top: 0; width: 380px; height: 270px; }
  .spread .page.left { left: 0; }
  .spread .page.right { left: 380px; box-shadow: inset 6px 0 8px -6px rgba(0,0,0,0.25); }

  .page-number {
    position: absolute; right: 10px; bottom: 8px; width: 9px; height: 9px;
    background: var(--ink-dark); color: var(--white); font-size: 6px; line-height: 9px; text-align: center;
  }

  /* Covers */
  .back-cover { background: linear-gradient(135deg, var(--red-dark) 0%, var(--red) 45%, var(--red-light) 100%); }
  .back-cover .wordmark {
    position: absolute; top: 22px; left: 24px; font-weight: 800; font-size: 24px; color: var(--white);
  }
  .back-cover .contact {
    position: absolute; right: 26px; bottom: 24px; text-align: right; color: var(--white);
    font-size: 6.5px; line-height: 1.45;
  }
  .back-cover .contact .web { margin-top: 8px; font-weight: 700; font-size: 7px; }
  .front-cover { background: linear-gradient(180deg, var(--page-light), var(--page)); }
  .front-cover .backdrop {
    position: absolute; top: 0; left: 0; width: 100%; height: 90px;
    background: linear-gradient(90deg, #e4e5e7, #f1f1f2);
  }
  .front-cover .wordmark {
    position: absolute; top: 48px; right: 26px; font-weight: 800; font-size: 26px; color: var(--red);
  }
  .front-cover .hero {
    position: absolute; left: 0; top: 92px; width: 372px; height: 178px;
    background: linear-gradient(160deg, #1c4f86 0%, #3f83b8 35%, #b9d8e6 55%, #2f6aa0 75%, #173a68 100%);
  }

  /* Spread 1 */
  .about { background: linear-gradient(120deg, #dcdcde 0%, #f4f4f5 60%, #e8e8e9 100%); }
  .about .tab { position: absolute; left: 14px; top: 150px; width: 8px; height: 26px; background: var(--ink-dark); }
  .about .heading { position: absolute; left: 30px; top: 153px; font-weight: 300; font-size: 13px; color: var(--red); }
  .about .red-box {
    position: absolute; left: 150px; top: 62px; width: 230px; height: 150px; padding: 12px 14px;
    background: linear-gradient(135deg, var(--red), var(--red-light)); color: var(--white);
    font-size: 5.5px; line-height: 1.5;
  }
  .about .red-box p { margin-bottom: 5px; }
  .about .red-box .strong { font-weight: 700; }
  .about .red-box ul { list-style: none; margin-bottom: 5px; }
  .about .red-box li::before { content: "■ "; font-size: 4px; }
  .intro { background: linear-gradient(90deg, #e9e9ea, #f7f7f7); }
  .intro .photo {
    position: absolute; left: 24px; top: 88px; width: 112px; height: 116px; border: 3px solid var(--white);
    background: linear-gradient(135deg, #1d3f8f 0%, #4d7ec4 45%, #b32a3c 70%, #e1e6ef 100%);
    box-shadow: 0 2px 5px rgba(0,0,0,0.2);
  }
  .intro .heading { position: absolute; left: 150px; top: 78px; font-weight: 300; font-size: 13px; color: var(--red); }
  .intro .body { position: absolute; left: 150px; top: 100px; width: 212px; font-size: 5.5px; line-height: 1.5; }
  .intro .body p { margin-bottom: 6px; }

  /* Spread 2 */
  .email-network { background: linear-gradient(120deg, #6a3b22 0%, #c58a55 35%, #e6c49a 55%, #9c5a33 80%, #5a2f1a 100%); }
  .email-network .scene { position: absolute; inset: 0; }
  .email-network .panel {
    position: absolute; left: 186px; top: 16px; width: 182px; height: 238px; padding: 6px 8px;
    background: rgba(255,255,255,0.22); color: var(--white); font-size: 5px; line-height: 1.45;
  }
  .email-network .panel h2 { font-weight: 300; font-size: 11px; margin: 4px 0 4px; }
  .email-network .panel h3 { font-weight: 700; font-size: 5.5px; margin: 5px 0 2px; }
  .email-network .panel p { margin-bottom: 4px; }
  .email-network .panel ul { list-style: none; }
  .email-network .panel li::before { content: "■ "; font-size: 4px; }
  .phones { background: linear-gradient(90deg, #e4e4e5, #eeeeef); }
  .phones .strip {
    position: absolute; left: 0; top: 0; width: 118px; height: 270px;
    background: linear-gradient(180deg, #e3dc3c 0%, #d8d034 60%, #c9c02d 100%);
  }
  .phones .content { position: absolute; left: 130px; top: 48px; width: 235px; font-size: 5px; line-height: 1.5; }
  .phones h2 { font-weight: 300; font-size: 13px; color: var(--red); margin-bottom: 6px; }
  .phones h3 { font-weight: 700; font-size: 5.5px; color: var(--ink-dark); margin: 6px 0 3px; }
  .phones p { margin-bottom: 5px; }
  .phones ul { list-style: none; }
  .phones li { margin-bottom: 3px; }
  .phones li::before { content: "■ "; font-size: 4px; }

  /* Spread 3 */
  .cloud-intro { background: linear-gradient(90deg, #dcdcdd, #ededee); }
  .cloud-intro h2 { position: absolute; left: 22px; top: 26px; font-weight: 300; font-style: italic; font-size: 11px; color: var(--red); }
  .cloud-intro .body { position: absolute; left: 22px; top: 46px; width: 222px; font-size: 5px; line-height: 1.5; }
  .cloud-intro .body p { margin-bottom: 5px; }
  .cloud-intro .chart {
    position: absolute; left: 22px; top: 196px; width: 82px; height: 44px; background: var(--white);
    border: 1px solid #d0d0d0;
  }
  .cloud-intro .note {
    position: absolute; left: 116px; top: 190px; width: 128px; height: 58px; padding: 7px 9px;
    background: #6c6f72; color: var(--white); font-size: 4.8px; line-height: 1.5;
  }
  .cloud-intro .feature-art {
    position: absolute; left: 256px; top: 18px; width: 124px; height: 128px;
    background: linear-gradient(135deg, #2fb7c6 0%, #1f8fa8 50%, #0f5e78 100%);
  }
  .cloud-intro .server-art {
    position: absolute; left: 256px; top: 150px; width: 124px; height: 100px;
    background: linear-gradient(135deg, #0d1f3c 0%, #22477a 55%, #0a1630 100%);
  }
  .cloud-detail { background: linear-gradient(90deg, #e6e6e7, #f3f3f4); }
  .cloud-detail .city {
    position: absolute; left: 0; top: 0; width: 380px; height: 118px;
    background: linear-gradient(180deg, #c9a98a 0%, #8e8a8d 45%, #5c6b7a 100%);
  }
  .cloud-detail .label {
    position: absolute; left: 16px; top: 34px; width: 150px; height: 72px; background: var(--red);
    display: flex; align-items: center; justify-content: center;
    font-weight: 800; font-size: 18px; color: var(--white);
  }
  .cloud-detail .banner {
    position: absolute; left: 166px; top: 34px; width: 214px; height: 72px; padding: 10px 12px;
    background: var(--slate); color: var(--white);
  }
  .cloud-detail .banner h2 { font-weight: 400; font-size: 10px; margin-bottom: 3px; }
  .cloud-detail .banner p { font-size: 5.5px; line-height: 1.45; text-transform: uppercase; letter-spacing: 0.3px; }
  .cloud-detail .columns {
    position: absolute; left: 16px; top: 130px; width: 350px; display: grid;
    grid-template-columns: repeat(3, 1fr); gap: 12px; font-size: 5px; line-height: 1.5;
  }
</style>
</head>
<body>
<div class="canvas">

  <div class="brand-title">Voltrane</div>

  <!-- Cover pair -->
  <section class="page back-cover" style="left:190px; top:200px; width:400px; height:283px;">
    <div class="wordmark">Voltrane</div>
    <address class="contact">
      ADDRESS 01<br>Harbour Road 12, Level 3<br>2000 Sydney, Australia<br>Telephone +61 2 5550 1234<br><br>
      ADDRESS 02<br>Kent Street 88, Suite 4<br>2000 Sydney, Australia<br>Telephone +61 2 5550 5678
      <div class="web">www.voltrane.com.au | social/voltrane</div>
    </address>
  </section>
  <section class="page front-cover" style="left:610px; top:200px; width:400px; height:283px;">
    <div class="backdrop" role="img" aria-label="Faint world map behind the cover title"></div>
    <div class="wordmark">Voltrane</div>
    <div class="hero" role="img" aria-label="Photograph of city towers at sunrise with an airliner and floating digital interface icons"></div>
  </section>

  <!-- About / Introduction -->
  <section class="spread" style="left:220px; top:600px;">
    <div class="page left about">
      <div class="tab"></div>
      <h2 class="heading">About Us</h2>
      <div class="red-box">
        <p>Founded in late 2005, Voltrane is a small, customer focused information technology company that focuses on helping small and medium businesses increase productivity through simple and effective technology solutions.</p>
        <p class="strong">Industries we have experience serving and supporting</p>
        <ul>
          <li>Medical – Physiotherapy, Dental &amp; General Practice</li>
          <li>Hospitality – Hotels, Restaurants &amp; Cafes</li>
          <li>Retail &amp; E-commerce</li>
          <li>Professional Services</li>
          <li>Trade Services</li>
        </ul>
        <p>From the outset we worked to provide small and medium business with great service, making information technology solutions that were simple, effective and affordable.</p>
      </div>
      <div class="page-number">2</div>
    </div>
    <div class="page right intro">
      <div class="photo" role="img" aria-label="Close-up photograph of network cables plugged into a switch"></div>
      <h2 class="heading">Introduction</h2>
      <div class="body">
        <p>Lorem ipsum is simply dummy text of the printing and typesetting industry. It has been the industry's standard dummy text ever since the 1500s, when an unknown printer took a galley of type and scrambled it.</p>
        <p>It was popularised in the 1960s with the release of sheets containing passages, and more recently with desktop publishing software including versions of it.</p>
        <p>Lorem ipsum is simply dummy text of the printing industry. It has survived not only five centuries, but also the leap into electronic typesetting, remaining essentially unchanged and ready for final copy.</p>
      </div>
      <div class="page-number">3</div>
    </div>
  </section>

  <!-- Communication -->
  <section class="spread" style="left:220px; top:960px;">
    <div class="page left email-network">
      <div class="scene" role="img" aria-label="Photograph of a tablet on a stand at a cafe counter with warm blurred background"></div>
      <div class="panel">
        <h2>Includes Email</h2>
        <p>A cloud based productivity suite that helps your team connect and get work done from anywhere on any device. It is simple to use and manage, so you can focus on what really matters.</p>
        <h2>Business Network</h2>
        <p>Having a secure, fast and reliable business network is imperative for all your connected devices to work for you.</p>
        <p>Your business network is the backbone of your technology, allowing your team to connect to data and services at the office or on the road.</p>
        <p>At Voltrane we offer a range of network services, from consulting on your requirements to implementation and support.</p>
        <h3>Network Services</h3>
        <ul>
          <li>Network consulting</li>
          <li>Managed networks</li>
          <li>Private IP networks</li>
          <li>Remote access</li>
          <li>Virtual private networks</li>
        </ul>
      </div>
      <div class="page-number">4</div>
    </div>
    <div class="page right phones">
      <div class="strip" role="img" aria-label="Photograph of a black telephone handset hanging by its coiled cord against a yellow wall"></div>
      <div class="content">
        <h2>Office Phones</h2>
        <h3>Big business phones at small business prices</h3>
        <p>Our digital office phones are designed for small businesses and deliver the features of a traditional PBX at a fraction of the price.</p>
        <p>You don't need any PBX hardware onsite, all you need are handsets, a router and a broadband connection. We provide you with everything to get up and running.</p>
        <h3>Is a Voltrane Business PBX the right solution for me?</h3>
        <p>Our digital office phones are an appropriate solution when:</p>
        <ul>
          <li>Your business is spread across sites but wishes to appear as one unified organisation with central call management.</li>
          <li>Your business wishes to use IP telephony without significant investment in hardware, software and support.</li>
          <li>You require a flexible phone system that lets staff move quickly between offices, home and overseas without disruption.</li>
        </ul>
      </div>
      <div class="page-number">5</div>
    </div>
  </section>

  <!-- Data & Storage -->
  <section class="spread" style="left:220px; top:1310px;">
    <div class="page left cloud-intro">
      <h2>Voltrane Data Cloud</h2>
      <div class="body">
        <p>Lorem ipsum is simply dummy text of the printing and typesetting industry. It has been the industry's standard dummy text ever since the 1500s, when an unknown printer took a galley of type and made a specimen book.</p>
        <p>It has survived not only five centuries, but also the leap into electronic typesetting, remaining essentially unchanged. It was popularised with sheets containing passages and desktop publishing software.</p>
      </div>
      <div class="chart" role="img" aria-label="Small illustration of storage charts and devices"></div>
      <div class="note">Tip: back up your business data daily and keep one copy offsite, so a single failure never stops your team from working.</div>
      <div class="feature-art" role="img" aria-label="Illustration of a person surrounded by floating cloud service icons on a teal background"></div>
      <div class="server-art" role="img" aria-label="Photograph of server rack cables glowing in blue light"></div>
      <div class="page-number">6</div>
    </div>
    <div class="page right cloud-detail">
      <div class="city" role="img" aria-label="Photograph of a city skyline at dusk"></div>
      <div class="label">Voltrane</div>
      <div class="banner">
        <h2>Voltrane Data Cloud</h2>
        <p>Lorem ipsum a step by step guide to running secure compliant and operationally efficient in NimbusCloud</p>
      </div>
      <div class="columns">
        <p>Lorem ipsum is simply dummy text of the printing and typesetting industry, used as a standard placeholder since the 1500s by printers and designers.</p>
        <p>Lorem ipsum is simply dummy text of the printing industry. It has survived five centuries and the leap into electronic typesetting unchanged.</p>
        <p>Lorem ipsum is simply dummy text of the printing and typesetting industry, popularised with sheets of passages and desktop publishing tools.</p>
      </div>
      <div class="page-number">7</div>
    </div>
  </section>

  <!-- Cover pair, second view -->
  <section class="page back-cover" style="left:250px; top:1680px; width:440px; height:311px;">
    <div class="wordmark">Voltrane</div>
    <address class="contact">
      ADDRESS 01<br>Harbour Road 12, Level 3<br>2000 Sydney, Australia<br>Telephone +61 2 5550 1234<br><br>
      ADDRESS 02<br>Kent Street 88, Suite 4<br>2000 Sydney, Australia<br>Telephone +61 2 5550 5678
      <div class="web">www.voltrane.com.au | social/voltrane</div>
    </address>
  </section>
  <section class="page front-cover" style="left:500px; top:1995px; width:440px; height:311px;">
    <div class="backdrop" role="img" aria-label="Faint world map behind the cover title"></div>
    <div class="wordmark" style="top:54px; font-size:28px;">Voltrane</div>
    <div class="hero" style="top:102px; width:410px; height:196px;" role="img" aria-label="Photograph of city towers at sunrise with an airliner and floating digital interface icons"></div>
  </section>

</div>
</body>
</html>
```